The Velmora Boutique Sticker Set

We are a flower shop who is creating a colorful DIY style box with cut flowers in a holograph bouquet paper. (Attached sample box)
Colors are yet to be finalized + the text inside too.
I am looking to include sticker sets with the flowers inside preferably as sticker sheets not individual stickers.
I need 3-5 Sticker Sheets and they can be icons, graphic images of flowers, quotes, words. I will include some of the ones I want as part of the set, feel free to suggest others.
Sticker Options:
1. Quotes
“ In an endless garden of flowers, I will always pick you”
“Velmora Club”
“Velmora at heart”
“You deserve flowers today and everyday”
“I got you flowers today”
“ You belong along the wildflowers”
“I must have flowers always & always”
Option for a sheet with horoscope flowers? Each sign and a flower type
Option for Alphabets
Option for heart/flower cute stickers / logo inspired
Stickers can be gifted as part of the box or used to decorate the box since it will be raw carton.
I also potentially want a card that can be used with this box (plain) in which they can stick these stickers on + write a message.
Sticker sheet can be 10 x 15 / 20 x 10

```html
<!DOCTYPE html>
<html lang="en">
<head>
<meta charset="utf-8">
<title>The Velmora Boutique Sticker Set</title>
<link href="https://fonts.googleapis.com/css2?family=Montserrat:wght@400;500;600;700;800&family=Abril+Fatface&family=Shrikhand&family=Chewy&family=Sniglet:wght@800&display=swap" rel="stylesheet">
<style>
:root{
  --cream:#fdf6e4;
  --rule:#b06a62;
  --ink:#2e2a28;
  --card-taupe:#e1d7cd;
  --card-border:#a4675d;
  --rose-red:#e05a68;
  --rose-text:#e06a78;
  --blush:#f5d9cd;
  --blush-soft:#f2d2cb;
  --pale-text:#f1c3c5;
  --white:#fdfdfd;
  --hot-pink:#f47c9b;
  --violet:#7b5fc9;
  --black:#111;
  --mustard:#f6d27a;
  --rust:#c0512e;
  --orchid:#e39ad2;
  --lavender:#b7aef2;
  --lime:#e8f56e;
  --petal:#f4c8d8;
  --sun:#ecd64a;
  --coral:#e84d6a;
}
*{box-sizing:border-box;margin:0;padding:0}
html,body{width:1200px;height:2939px;overflow:hidden}
body{background:var(--cream);position:relative;font-family:"Montserrat",sans-serif;color:var(--ink)}
.section-title{position:absolute;left:0;width:1200px;display:flex;align-items:center;font-size:25px;font-weight:400}
.section-title .rule{height:1.5px;background:var(--rule)}
.section-title span{padding:0 12px;white-space:nowrap}

.sticker{position:absolute;display:flex;align-items:center;justify-content:center;text-align:center}
.sticker-art{position:absolute;inset:0;border-radius:46% 54% 48% 52% / 52% 46% 54% 48%;box-shadow:6px 8px 10px rgba(0,0,0,.18)}
.sticker-quote{position:relative;white-space:nowrap}
.quote-club{font-family:"Shrikhand",serif;font-size:78px;line-height:82px;color:var(--mustard);text-shadow:4px 4px 0 #8e3418;transform:rotate(-6deg)}
.quote-club span{display:block;padding-left:110px}
.quote-always{font-family:"Shrikhand",serif;font-size:44px;line-height:52px;color:#f7d3ee;text-shadow:3px 3px 0 #c46fae;transform:rotate(-3deg);margin-top:-40px}
.quote-always .small{font-size:36px}
.quote-heart{font-family:"Chewy",sans-serif;font-size:72px;line-height:70px;color:var(--lime);text-shadow:3px 4px 0 #6f5cc4;transform:rotate(-5deg)}
.quote-wild{font-family:"Sniglet",sans-serif;font-weight:800;font-size:50px;line-height:54px;letter-spacing:3px;color:var(--sun);text-shadow:2px 3px 0 #8a5a52;transform:rotate(-3deg);margin-top:40px}
.quote-deserve{font-family:"Chewy",sans-serif;font-size:56px;line-height:56px;color:var(--coral);text-shadow:2px 3px 0 #fff;transform:rotate(-2deg);margin-top:70px}

.card{position:absolute;width:487px;height:325px;box-shadow:6px 8px 10px rgba(0,0,0,.15)}
.card-taupe{background:var(--card-taupe)}
.card-taupe::after{content:"";position:absolute;inset:7px;border:2px solid var(--card-border)}
.thanks-serif{position:absolute;left:32px;top:98px;font-family:"Abril Fatface",serif;font-size:78px;color:var(--rose-red);letter-spacing:-2px;text-shadow:3px 3px 0 #8f4a4a}
.for-order{position:absolute;left:172px;top:214px;display:flex;align-items:center;gap:6px;font-size:16px;color:#8a5a52}
.for-order i{display:block;width:118px;height:1.5px;background:#8a5a52}
.handle{position:absolute;left:0;right:0;top:282px;display:flex;justify-content:center;align-items:center;gap:5px;font-size:13px;color:#7a5450}
.handle b{width:11px;height:11px;border:1.5px solid #7a5450;border-radius:50%}
.card-name{position:absolute;left:0;right:0;top:106px;text-align:center;font-size:17px;font-weight:600;letter-spacing:2px;line-height:21px;color:var(--rose-text)}
.write-line{position:absolute;left:48px;width:390px;height:2px;background:var(--card-border)}
.card-blush{background:var(--blush);overflow:hidden}
.thanks-script{position:absolute;left:80px;top:40px;font-family:"Shrikhand",serif;font-size:86px;line-height:90px;color:var(--white);text-shadow:4px 4px 0 #f0c9bd}
.thanks-script span{display:block;padding-left:130px}
.card-white{background:var(--white)}
.card-white .card-name{color:var(--pale-text)}
.card-white .write-line{background:#f3d9d8;height:1.5px}

.wrap-paper{position:absolute;left:82px;top:2127px;width:756px;height:751px;background:var(--blush)}
.round{position:absolute;width:240px;height:240px;border-radius:50%;box-shadow:5px 7px 10px rgba(0,0,0,.2);overflow:hidden}
.round svg{width:100%;height:100%;display:block}
</style>
</head>
<body>

<div class="section-title" style="top:35px"><i class="rule" style="margin-left:55px;width:424px"></i><span>Stickers Collection</span><i class="rule" style="width:424px"></i></div>

<div class="sticker" style="left:55px;top:97px;width:498px;height:257px">
  <div class="sticker-art" role="img" aria-label="Retro sticker shape in rust with cream outline and sparkles" style="background:linear-gradient(135deg,#d9733f,var(--rust))"></div>
  <p class="sticker-quote quote-club">Velmora<span>Club</span></p>
</div>

<div class="sticker" style="left:639px;top:97px;width:485px;height:268px">
  <div class="sticker-art" role="img" aria-label="Pink sticker shape with two small red flowers below the text" style="background:linear-gradient(160deg,#e7a7d8,#e58cc0)"></div>
  <p class="sticker-quote quote-always"><span class="small">I Must Have</span><br>Flowers Always<br>and Always</p>
</div>

<div class="sticker" style="left:74px;top:399px;width:456px;height:314px">
  <div class="sticker-art" role="img" aria-label="Watercolour sticker of a pink and a blue peony with grey leaves on a yellow outline" style="background:linear-gradient(120deg,#f1d98a,#e7b6b6 45%,#a9c1dc)"></div>
</div>

<div class="sticker" style="left:639px;top:422px;width:393px;height:251px">
  <div class="sticker-art" role="img" aria-label="Lavender sticker shape with purple flower sprigs" style="background:linear-gradient(135deg,#c6b9f0,var(--lavender))"></div>
  <p class="sticker-quote quote-heart">Velmora<br>at heart</p>
</div>

<div class="sticker" style="left:103px;top:741px;width:433px;height:434px">
  <div class="sticker-art" role="img" aria-label="Sticker shape framed by a pink and lilac bouquet with a blue flower below" style="background:linear-gradient(170deg,#e6b5b9,#f8dde8 55%,#c9d4e6)"></div>
  <p class="sticker-quote quote-wild">YOU BELONG<br>ALONG THE<br>WILDFLOWERS</p>
</div>

<div class="sticker" style="left:667px;top:798px;width:400px;height:320px">
  <div class="sticker-art" role="img" aria-label="Yellow and lilac sticker shape topped with a spray of wildflowers" style="background:linear-gradient(170deg,#c9b4ee,#f4dd6a 40%,#f7e49a)"></div>
  <p class="sticker-quote quote-deserve">you deserve<br>flowers today<br>and everday</p>
</div>

<div class="section-title" style="top:1227px"><i class="rule" style="margin-left:55px;width:424px"></i><span>Thankyou Card</span><i class="rule" style="width:424px"></i></div>

<div class="card card-taupe" style="left:106px;top:1306px">
  <div class="thanks-serif">Thank You</div>
  <div class="for-order"><i></i>For Your Order</div>
  <div class="handle"><b></b>thevelmoraboutique</div>
</div>
<div class="card card-taupe" style="left:616px;top:1306px">
  <div class="card-name">THE VELMORA BOUTIQUE<br>DUBAI</div>
  <i class="write-line" style="top:182px"></i>
  <i class="write-line" style="top:210px"></i>
  <i class="write-line" style="top:241px"></i>
</div>
<div class="card card-blush" style="left:106px;top:1663px">
  <div class="thanks-script">Thank<span>You</span></div>
</div>
<div class="card card-white" style="left:619px;top:1663px">
  <div class="card-name">THE VELMORA BOUTIQUE<br>DUBAI</div>
  <i class="write-line" style="top:193px"></i>
  <i class="write-line" style="top:221px"></i>
  <i class="write-line" style="top:253px"></i>
</div>

<div class="section-title" style="top:2052px"><i class="rule" style="margin-left:74px;width:371px"></i><span>paper &amp; Round Stickers</span><i class="rule" style="width:371px"></i></div>

<div class="wrap-paper" role="img" aria-label="Blush wrapping paper with a repeating white floral pattern"></div>

<div class="round" style="left:863px;top:2113px;background:var(--blush-soft)">
  <svg viewBox="0 0 240 240">
    <circle cx="120" cy="120" r="112" fill="none" stroke="#fbe6e2" stroke-width="3"/>
    <defs><path id="arcRing" d="M43.8,164 A88,88 0 1,1 196.2,164"/></defs>
    <text font-family="Montserrat, sans-serif" font-size="18" fill="#fbeeea" letter-spacing="2"><textPath href="#arcRing" startOffset="50%" text-anchor="middle">THE VELMORA BOUTIQUE</textPath></text>
    <text x="120" y="206" text-anchor="middle" font-family="Montserrat, sans-serif" font-size="20" fill="#fbeeea" letter-spacing="3">DUBAI</text>
  </svg>
</div>
<div class="round" style="left:868px;top:2387px;background:var(--white);border:9px solid var(--black)">
  <svg viewBox="9 9 222 222">
    <text text-anchor="middle" font-family="Montserrat, sans-serif" font-weight="800" font-size="25" fill="#e0417f"><tspan x="120" y="108">THE</tspan><tspan x="120" y="136">VELMORA</tspan><tspan x="120" y="164">BOUTIQUE</tspan></text>
  </svg>
</div>
<div class="round" style="left:868px;top:2652px;background:var(--hot-pink)">
  <svg viewBox="0 0 240 240">
    <circle cx="120" cy="120" r="98" fill="none" stroke="#7b5fc9" stroke-width="6"/>
    <text text-anchor="middle" font-family="Montserrat, sans-serif" font-weight="600" font-size="20" fill="#fff"><tspan x="120" y="114">VELMORA</tspan><tspan x="120" y="140">BOUTIQUE</tspan></text>
  </svg>
</div>

</body>
</html>
```